Morvex Business Card (intended for Business Card sized magnet)

Hi guys,

I would like to get a design for my business card for the restaurant. The design must be single sided as I intend to produce business card sized magnets.

The File attached must me on and I'm open for new ides

Can you please ensure that the design meets Cardowell's magnetic business card size specifications:

http://www.cardowell.example.au/custom-magnets.aspx?txi=15695&xnid=TopNav_Magnetic+Business+Cards+(linked+item)_Magnets_Marketing+Products&xnav=TopNav

Full Bleed Size (starting document size):
90 x 52 mm
1062 x 615 pixels
* Finished artwork should use the full bleed dimensions for best results.

Document Trim Size (final size after being cut):
87 x 49 mm
1028 x 579 pixels
* Please be sure to keep all text within the safe margin.

Resolution:
300 DPI

The winning design/source files need to meet these specifications.

Thanks
Updates

Hi guys, can I see more options please Thanks

```html
<!DOCTYPE html>
<html lang="en">
<head>
<meta charset="utf-8">
<title>Morvex Business Card</title>
<link rel="stylesheet" href="https://fonts.googleapis.com/css2?family=Gilda+Display&family=Libre+Baskerville:ital@1&family=Oswald:wght@600&family=Questrial&display=swap">
<style>
  :root {
    --ink: #0c0c0c;
    --paper: #ffffff;
    --gold: #f6b80d;
    --text: #111111;
    --ornament: #3a3a3a;
  }
  * { margin: 0; padding: 0; box-sizing: border-box; }
  html, body { width: 1200px; height: 693px; overflow: hidden; background: var(--paper); }
  .card { position: relative; width: 1200px; height: 693px; background: var(--paper); }
  .card__top { position: absolute; left: 0; top: 0; width: 1200px; height: 487px; background: var(--ink); }
  .card__text { position: absolute; line-height: 1; white-space: nowrap; }
  .exec-name {
    left: 63px; top: 54px; font: italic 22px "Libre Baskerville", serif; color: var(--paper);
  }
  .call-now {
    right: 52px; top: 50px; color: var(--gold); font: 45px "Gilda Display", serif;
  }
  .call-now__number { font: 600 46px "Oswald", sans-serif; letter-spacing: 0.5px; }
  .wordmark {
    left: 0; width: 1200px; text-align: center; top: 192px;
    font: 112px "Gilda Display", serif; color: var(--paper);
  }
  .ornament-band { position: absolute; left: 422px; top: 308px; }
  .restaurant-name {
    left: 63px; top: 512px; font: 54px "Gilda Display", serif; color: var(--text);
  }
  .address {
    left: 68px; top: 580px; font: 31px "Questrial", sans-serif; color: var(--text);
  }
  .hours {
    left: 68px; top: 624px; font: 25px "Questrial", sans-serif; color: var(--text);
  }
</style>
</head>
<body>
  <div class="card">
    <div class="card__top"></div>
    <p class="card__text exec-name">Executive name</p>
    <p class="card__text call-now">Call Now - <span class="call-now__number">03 9418 2730</span></p>
    <p class="card__text wordmark">Morvex</p>
    <svg class="ornament-band" width="378" height="140" viewBox="0 0 378 140">
      <rect x="0" y="4" width="378" height="4" fill="#ffffff"/>
      <rect x="0" y="24" width="378" height="92" fill="var(--ornament)" role="img" aria-label="Geometric star ornament band with three coloured centre dots"/>
      <rect x="0" y="132" width="378" height="4" fill="#ffffff"/>
    </svg>
    <p class="card__text restaurant-name">Morvex Restrurant</p>
    <p class="card__text address">Address : 412 Harlow Rd, Brenton South ,3170</p>
    <p class="card__text hours">Opening Hours : Sunday - Friday 11:30 -9:30, Saturday from 5:30 -10.00</p>
  </div>
</body>
</html>
```